Epoxy coatings company needs a logo/business card design.

My company name is "Lustrous Resin Works", and I am looking for a company logo and business card design.
My initial thought was to use "Æ"in 'Lu'strous, and would also like to see ideas on how to play around with the fact that the first 3 letters (Lrw) are also the acronym of the company name.
I specialize in garage floor and interior epoxy coatings, paint flake broadcasts, quartz broadcasts, and solid color epoxy floors, concrete repairs.
I like images I've seen of a silhouetted person running a floor grinder. It keeps the design of the card simple. I'm not necessarily opposed to using images of the floors on the card, but I'd prefer to keep the front simple (Company name, my name, phone number, email) and maybe put pictures on the back. I've included a few of my personal pictures of floors I've done (including a before, after, and when the garage was being used after)
My colors are darker green (Fern/Forest/Hunter, etc), and Bronze.

Contact Information for Business Card

Name: Dana Kellworth Email: lustrousresinworks@mailbrook.net Phone: (555)318-9042 Instagram: lustrous_resin_works

Colors

Designer to choose colors to be used in the design.

Requirements
Nice to have
• I've included a business card designed for someone else, that contains the silhouette that I'm looking for. The floor grinder that I use is large like the one pictured (Torvex G40R).

```html
<!DOCTYPE html>
<html lang="en">
<head>
<meta charset="utf-8">
<title>Lustrous Resin Works – Business Card</title>
<link href="https://fonts.googleapis.com/css2?family=Montserrat:wght@400;500;700&display=swap" rel="stylesheet">
<style>
  :root {
    --forest: #3e4a21;
    --bronze: #d99c5a;
    --white: #ffffff;
    --backdrop: #e4e1d8;
    --stone-dark: #6b6d6c;
    --stone-mid: #9a9c9b;
    --stone-light: #b9bbba;
  }
  * { box-sizing: border-box; margin: 0; padding: 0; }
  html, body {
    width: 1200px; height: 1200px; overflow: hidden;
    background: var(--backdrop);
    font-family: "Montserrat", sans-serif;
  }
  .canvas { position: relative; width: 1200px; height: 1200px; }
  .card {
    position: absolute; left: 150px; width: 900px; height: 500px;
    background: var(--forest); overflow: hidden;
    box-shadow: 0 6px 18px rgba(0,0,0,0.18);
  }
  .card--front { top: 75px; }
  .card--back { top: 625px; }
  .rule { position: absolute; height: 5px; background: var(--bronze); }
  .divider-bar { position: absolute; left: 385px; top: 0; width: 75px; height: 500px; background: var(--bronze); }

  .brand-name {
    position: absolute; color: var(--bronze); font-weight: 700;
    text-transform: uppercase; letter-spacing: 1px; line-height: 1.15;
  }
  .card--front .brand-name { left: 50px; top: 95px; width: 320px; font-size: 34px; }
  .card--back .brand-name { left: 440px; top: 80px; width: 420px; font-size: 42px; }

  .silhouette { position: absolute; background: var(--bronze); opacity: 0.9; border-radius: 6px; }
  .card--front .silhouette { left: 75px; top: 265px; width: 270px; height: 205px; }
  .card--back .silhouette { left: 135px; top: 30px; width: 220px; height: 190px; }

  .person { position: absolute; left: 495px; top: 95px; }
  .person__name { color: var(--white); font-weight: 700; font-size: 28px; letter-spacing: 3px; text-transform: uppercase; }
  .person__role { color: var(--bronze); font-weight: 400; font-size: 22px; letter-spacing: 3px; text-transform: uppercase; margin-top: 4px; }

  .contact-icon {
    position: absolute; left: 394px; width: 56px; height: 56px; border-radius: 50%;
    background: var(--white); display: flex; align-items: center; justify-content: center;
  }
  .contact-icon--phone { top: 300px; }
  .contact-icon--mail { top: 365px; }
  .contact-text { position: absolute; left: 500px; color: var(--white); font-size: 21px; font-weight: 400; }
  .contact-text--phone { top: 313px; }
  .contact-text--mail { top: 378px; font-size: 19px; }

  .services {
    position: absolute; left: 120px; top: 290px; list-style: none;
    color: var(--white); font-size: 24px; line-height: 1.3;
  }
  .finishes { position: absolute; left: 455px; top: 310px; display: flex; gap: 12px; }
  .finish { width: 138px; height: 145px; }
  .finish--flake-dark { background: linear-gradient(135deg, var(--stone-dark), var(--stone-mid)); }
  .finish--flake-light { background: linear-gradient(135deg, var(--stone-light), var(--stone-dark)); }
  .finish--quartz { background: linear-gradient(135deg, var(--stone-mid), var(--stone-dark)); }
</style>
</head>
<body>
<main class="canvas">

  <section class="card card--front" aria-label="Business card front">
    <div class="rule" style="left:0; top:45px; width:385px;"></div>
    <div class="rule" style="left:0; top:225px; width:385px;"></div>
    <div class="rule" style="left:460px; top:45px; width:440px;"></div>
    <div class="rule" style="left:460px; top:205px; width:440px;"></div>
    <div class="divider-bar"></div>

    <div class="brand-name">Lustrous Resin Works</div>
    <div class="silhouette" role="img" aria-label="Silhouette of a worker pushing a large floor grinder"></div>

    <div class="person">
      <div class="person__name">Dana Kellworth</div>
      <div class="person__role">Manager</div>
    </div>

    <div class="contact-icon contact-icon--phone">
      <svg width="28" height="28" viewBox="0 0 24 24" aria-hidden="true">
        <path fill="var(--forest)" d="M6.6 10.8a15.1 15.1 0 0 0 6.6 6.6l2.2-2.2a1 1 0 0 1 1-.25 11.4 11.4 0 0 0 3.6.57 1 1 0 0 1 1 1V20a1 1 0 0 1-1 1A17 17 0 0 1 3 4a1 1 0 0 1 1-1h3.5a1 1 0 0 1 1 1c0 1.25.2 2.45.57 3.6a1 1 0 0 1-.25 1z"/>
      </svg>
    </div>
    <div class="contact-text contact-text--phone">(555)318-9042</div>

    <div class="contact-icon contact-icon--mail">
      <svg width="32" height="24" viewBox="0 0 32 24" aria-hidden="true">
        <rect x="2" y="3" width="28" height="18" fill="none" stroke="var(--forest)" stroke-width="1.8"/>
        <polyline points="2,3 16,14 30,3" fill="none" stroke="var(--forest)" stroke-width="1.8"/>
        <polyline points="2,21 12,11 M30,21 20,11" fill="none" stroke="var(--forest)" stroke-width="1.5"/>
        <line x1="2" y1="21" x2="12.5" y2="11" stroke="var(--forest)" stroke-width="1.5"/>
        <line x1="30" y1="21" x2="19.5" y2="11" stroke="var(--forest)" stroke-width="1.5"/>
      </svg>
    </div>
    <div class="contact-text contact-text--mail">lustrousresinworks@mailbrook.net</div>
  </section>

  <section class="card card--back" aria-label="Business card back">
    <div class="silhouette" role="img" aria-label="Silhouette of a worker pushing a large floor grinder"></div>
    <div class="brand-name">Lustrous Resin Works</div>
    <div class="rule" style="left:0; top:245px; width:900px;"></div>

    <ul class="services">
      <li>Garage floors</li>
      <li>Interior epoxy coatings</li>
      <li>Paint flake broadcasts</li>
      <li>Quartz broadcasts</li>
      <li>Solid color epoxy floors</li>
    </ul>

    <div class="finishes">
      <div class="finish finish--flake-dark" role="img" aria-label="Photo of a dark grey paint flake epoxy floor"></div>
      <div class="finish finish--flake-light" role="img" aria-label="Photo of a light grey and white paint flake epoxy floor"></div>
      <div class="finish finish--quartz" role="img" aria-label="Photo of a grey quartz broadcast floor"></div>
    </div>
  </section>

</main>
</body>
</html>
```